Interior Design for Every Hour, Mara Velbourne Interior Design, LLC

We are looking for a website for an Interior Design Company targeted at higher income households. We prefer to work with clients that seek to amplify the architectural beauty of their interior space via interior design - while ensuring the space promotes easy living. For example: a kitchen should be lain out in an intuitive manner such that all utensils, cups and plates are easy to find. Living rooms should be arranged to promote conversation and/or watch TV, etc.... We have heavy reliance on the technical aspects of design (computer automated renderings). We like the look and feel of this website: https://www.jorvenstudio.com/portfolioall

Target Market(s)

Upper HHI ($200,000+) in the Atlanta Metro Market. Customers are likely to be highly educated and from a variety of cultural backgrounds. Ages 35-60

Font styles to use
Sans Serif

Colors

Designer to choose colors to be used in the design.

Requirements
Must have
• Landing Page, Page demonstrating how interior design fits into the architectural design process, About Us Page with contact info, Example Work Page and Tailored Client Page. Minimal work can be done on the About Us and example work pages. The tailored client page just needs a good layout (and easy uploads and download capability)
• Also to include:
• (1) The landing page should include a Design Philosophy Section and maybe a couple examples of our work and/or pictures you provide
• (2) The Design Process page should explain all steps of the architectural Design process and should explain where interior design/decorating fits into the Architectural process (see below attachments).
• (3) The Example work page should include areas for portfolio example uploads (to include 3 dimensional and 2 dimensional renderings, photos and videos).
• (4) Include a Password Protected, Secure Place where each individual client can store and retrieve documents and work product for their project (Should be a separate page). There should be sections (for each client) for:
• (a) there should be a client account creation requirement page that requires: FN, LN, Mobile, email, Work phone, Property address, City, Zip (for 3 properties), Spouse FN, Spouse LN, Child FN, LN (space for 5 children)
• (a) section: Legal & Invoices
• (b) section: Drawings & Renderings
• (c) section: Pin Ups (easy uploads of pictures from sites like snapweave would be appreciated) - pin ups should be very easy for clients to put examples of what they like
• (5) Ability for admin to use personalized password and username to view, delete and edit client files (we utilize filecrate for document storage currently, and integration with filecrate would be a plus)
• (6) needs to be formatted and optimized for Mobile (iOs and android) viewing as well as Web
• (7) The site should be built with a hosting service contemplated. This service should be affordable (Less than $300 per annum)
• (8) most importantly the site should be minimalist with focus on user friendliness while being fashion forward
• (9) Website Color scheme should be White/Black/BlueGrey
• (10) The site must also include the ability to generate an invoice, based on client registration, electronically submit the invoice to the client via email (or print it), accept payment via coinrelay integration, and generate conformation email of payment to both client and admin (although coinrelay may already do this).
Nice to have
• Ability of example and client pages to be integrated with sites like snapwev and filecrate. Ability to have some sort of section that self identifies the clients design style(s)...maybe a quiz or at lease a place where they can create a pinboard of images and colors they like (potentially by room)
Should not have
• Must look modern and be extremely quick/user friendly. Our clients are very busy.

```html
<!DOCTYPE html>
<html lang="en">
<head>
<meta charset="utf-8">
<title>Mara Velbourne Interior Design, LLC</title>
<link href="https://fonts.googleapis.com/css2?family=Poppins:wght@300;400;500;600;700&display=swap" rel="stylesheet">
<style>
:root{
  --ink:#111111;
  --text:#333333;
  --muted:#8a8a8a;
  --faint:#c9c9c9;
  --line:#e4e4e4;
  --panel:#f4f4f4;
  --white:#ffffff;
  --hero-a:#2a2420;
  --hero-b:#6d625a;
}
*{margin:0;padding:0;box-sizing:border-box}
html,body{width:1200px;height:2936px;overflow:hidden;background:var(--white)}
body{position:relative;font-family:'Poppins',sans-serif;color:var(--text)}
.abs{position:absolute}
a{color:inherit;text-decoration:none}

/* header */
.brand-row{left:78px;top:26px;display:flex;align-items:baseline;gap:16px;white-space:nowrap}
.brand{font-size:22px;font-weight:700;letter-spacing:1px;color:var(--ink)}
.brand-sub{font-size:11px;color:var(--faint);letter-spacing:.5px}
.nav{left:526px;top:32px;display:flex;gap:24px;font-size:13px;font-weight:500;color:var(--ink);align-items:center;white-space:nowrap}
.nav .current{color:var(--faint)}
.client-btn{left:1032px;top:24px;width:116px;height:36px;border:1px solid var(--line);font-size:13px;font-weight:500;color:var(--ink);display:flex;align-items:center;justify-content:center}

/* hero */
.hero{left:78px;top:81px;width:1070px;height:526px;background:linear-gradient(120deg,var(--hero-a),var(--hero-b) 55%,#3b332d)}
.hero-frame{left:236px;top:177px;width:206px;height:344px;border:3px solid var(--white)}
.hero-kicker{left:288px;top:228px;font-size:13px;color:var(--white)}
.hero-title{left:288px;top:258px;font-size:40px;font-weight:500;line-height:48px;color:var(--white);white-space:nowrap}
.hero-link{left:288px;top:452px;font-size:13px;color:var(--white)}
.hero-dots{left:910px;top:455px;display:flex;gap:18px}
.hero-dots span{width:5px;height:5px;background:var(--white)}

/* about */
.label{font-size:12px;color:var(--ink);font-weight:500}
.heading{font-size:25px;font-weight:600;color:var(--ink);line-height:34px}
.about-label{left:234px;top:708px}
.about-heading{left:234px;top:740px;width:380px}
.about-text{left:234px;top:826px;width:370px;font-size:12px;line-height:18px;color:var(--muted)}
.more-link{left:234px;top:1020px;font-size:12px;font-weight:500;color:var(--ink)}
.about-photo{left:704px;top:712px;width:288px;height:330px;background:linear-gradient(160deg,#4a5260,#2b2a2c 60%,#5a4a3e)}

/* process */
.process-ghost{left:0;width:1200px;top:1108px;text-align:center;font-size:56px;font-weight:600;color:#f3f3f3}
.process-label{left:0;width:1200px;top:1146px;text-align:center}
.step{top:1206px;width:240px;text-align:center}
.step-circle{margin:0 auto;width:122px;height:122px;border-radius:50%;border:2px solid var(--line);display:flex;align-items:center;justify-content:center;background:var(--white)}
.step-circle.active{background:var(--ink);border-color:var(--ink)}
.step-num{position:absolute;top:-4px;left:176px;font-size:14px;color:var(--faint);font-weight:500}
.step-name{margin-top:14px;font-size:13px;font-weight:600;color:var(--ink);line-height:20px}
.flow-arrow{top:1262px}
.nav-circle{width:24px;height:24px;border-radius:50%;border:1px solid var(--faint);display:flex;align-items:center;justify-content:center}
.explore-btn{left:556px;top:1418px;width:114px;height:32px;border:1px solid var(--line);font-size:12px;font-weight:500;color:var(--ink);display:flex;align-items:center;justify-content:center}

/* work */
.work-panel{left:78px;top:1544px;width:1070px;height:634px;background:var(--panel)}
.work-label{left:234px;top:1628px}
.work-heading{left:234px;top:1656px}
.view-link{font-size:12px;font-weight:500;color:var(--ink)}
.work-view{left:856px;top:1664px}
.project{top:1714px;width:522px;height:370px}
.project-a{left:78px;background:linear-gradient(135deg,#e8e8e6,#b9b8b4 60%,#8f8a82)}
.project-b{left:626px;background:linear-gradient(135deg,#6a6660,#8c887f 50%,#bfbbb3)}
.project-title{font-size:15px;font-weight:600;color:var(--white)}
.project-text{font-size:12px;line-height:18px;color:var(--white);width:420px}
.project-link{font-size:12px;color:var(--white)}
.work-dots{left:572px;top:2128px;display:flex;gap:12px}
.work-dots span{width:5px;height:5px;border-radius:50%;background:var(--faint)}
.work-dots span.on{background:var(--ink)}

/* testimonials */
.test-label{left:234px;top:2282px}
.test-heading{left:234px;top:2314px}
.test-view{left:912px;top:2316px;color:var(--faint)}
.quote{top:2406px;width:356px;height:182px;border:1px solid var(--line)}
.avatar{position:absolute;left:22px;top:-30px;width:54px;height:54px;border-radius:50%;background:linear-gradient(160deg,#8b8b8b,#2c2c2c)}
.quote-name{position:absolute;left:22px;top:40px;font-size:15px;font-weight:600;color:var(--ink);white-space:nowrap}
.quote-name small{font-size:11px;font-weight:400;color:var(--faint)}
.quote-text{position:absolute;left:22px;top:68px;width:316px;font-size:12px;line-height:20px;color:var(--muted)}

/* footer */
.footer-rule{left:54px;top:2680px;width:1118px;height:3px;background:#ececec}
.copyright{left:78px;top:2766px;font-size:11px;color:var(--ink)}
.foot-brand-row{left:78px;top:2790px;display:flex;align-items:baseline;gap:14px;white-space:nowrap}
.foot-brand{font-size:19px;font-weight:700;letter-spacing:1px;color:var(--ink)}
.foot-sub{font-size:11px;color:var(--faint)}
.foot-rights{left:78px;top:2842px;font-size:11px;color:var(--faint)}
.foot-list{top:2792px;font-size:12px;line-height:21px;color:var(--ink);list-style:none}
.contact-phone{left:914px;top:2790px;font-size:15px;font-weight:600;color:var(--ink);display:flex;gap:10px;align-items:center;white-space:nowrap}
.contact-mail{left:914px;top:2816px;font-size:12px;color:var(--ink);display:flex;gap:10px;align-items:center;white-space:nowrap}
.socials{left:916px;top:2868px;display:flex;gap:22px}
.socials span{width:24px;height:24px;border:1px solid var(--faint);transform:rotate(45deg);background:var(--white)}
.socials span.on{background:var(--ink);border-color:var(--ink)}
</style>
</head>
<body>

<header>
  <div class="abs brand-row">
    <div class="brand">MARA VELBOURNE</div>
    <div class="brand-sub">INTERIOR DESIGN LLC</div>
  </div>
  <nav class="abs nav">
    <svg width="12" height="12" viewBox="0 0 12 12"><path d="M6 1 L11 6 H9.5 V11 H7 V8 H5 V11 H2.5 V6 H1 Z" fill="#111"/></svg>
    <a>Our Story</a><a>Work</a><a class="current">Design Process</a><a>Testimonials</a><a>Contact</a>
  </nav>
  <a class="abs client-btn">Client Login</a>
</header>

<section>
  <div class="abs hero" role="img" aria-label="Photo of a luxury bedroom with a wide upholstered bed, wood panelling and a large window"></div>
  <div class="abs hero-frame"></div>
  <div class="abs hero-kicker">Residential</div>
  <h1 class="abs hero-title">The luxury<br>home interior<br>design</h1>
  <a class="abs hero-link">See Project &nbsp;→</a>
  <div class="abs hero-dots"><span></span><span></span><span></span><span></span></div>
</section>

<section>
  <div class="abs label about-label">About Us</div>
  <h2 class="abs heading about-heading">We are the leader in the interior design</h2>
  <p class="abs about-text">Creation, execution and completion of architectural and interiors projects working with private clients, architects, engineers, LEED experts, and community planners in accordance with building life safety codes, city zoning laws and ADA requirements. Selection, coordination and installation of furniture, fixtures &amp; equipment. Space planning, 3D modeling, construction document ...</p>
  <a class="abs more-link">More About Us &nbsp;→</a>
  <div class="abs about-photo" role="img" aria-label="Photo of a dark bedroom with a city view at dusk"></div>
</section>

<section>
  <div class="abs process-ghost">Design Process</div>
  <div class="abs label process-label">Our Work Flow</div>

  <div class="abs nav-circle" style="left:78px;top:1256px"><svg width="8" height="10" viewBox="0 0 8 10"><path d="M6 1 L2 5 L6 9" stroke="#bbb" fill="none" stroke-width="1.5"/></svg></div>
  <div class="abs nav-circle" style="left:1122px;top:1256px"><svg width="8" height="10" viewBox="0 0 8 10"><path d="M2 1 L6 5 L2 9" stroke="#777" fill="none" stroke-width="1.5"/></svg></div>

  <div class="abs step" style="left:92px">
    <span class="step-num">01.</span>
    <div class="step-circle"><svg width="44" height="50" viewBox="0 0 44 50"><rect x="4" y="6" width="36" height="42" rx="3" fill="none" stroke="#111" stroke-width="4"/><rect x="14" y="1" width="16" height="9" fill="#111"/><path d="M14 20 L30 36 M30 20 L14 36" stroke="#111" stroke-width="4"/></svg></div>
    <div class="step-name">Facility<br>Assessment</div>
  </div>
  <div class="abs step" style="left:360px">
    <span class="step-num">02.</span>
    <div class="step-circle active"><svg width="48" height="48" viewBox="0 0 48 48"><circle cx="22" cy="26" r="18" fill="none" stroke="#fff" stroke-width="4"/><circle cx="22" cy="26" r="10" fill="none" stroke="#fff" stroke-width="4"/><circle cx="22" cy="26" r="3" fill="#fff"/><path d="M22 26 L40 8 M36 4 L40 8 L44 6" stroke="#fff" stroke-width="3" fill="none"/></svg></div>
    <div class="step-name">Mission<br>and Vision</div>
  </div>
  <div class="abs step" style="left:626px">
    <span class="step-num">03.</span>
    <div class="step-circle"><svg width="48" height="48" viewBox="0 0 48 48"><path d="M6 14 L14 6 L42 34 L34 42 Z" fill="none" stroke="#111" stroke-width="4"/><path d="M8 40 L12 28 L34 6 L42 14 L20 36 Z" fill="#111"/></svg></div>
    <div class="step-name">Design &amp; Development<br>Direction</div>
  </div>
  <div class="abs step" style="left:894px">
    <span class="step-num">04.</span>
    <div class="step-circle"><svg width="50" height="50" viewBox="0 0 50 50"><path d="M25 2 L48 25 L25 48 L2 25 Z" fill="#111"/><path d="M13 13 L37 37 M19 7 L43 31 M7 19 L31 43 M37 13 L13 37 M31 7 L7 31 M43 19 L19 43" stroke="#fff" stroke-width="2"/></svg></div>
    <div class="step-name">Materials &amp; Furnishings<br>Selection</div>
  </div>

  <svg class="abs flow-arrow" style="left:326px" width="40" height="14" viewBox="0 0 40 14"><path d="M2 10 Q20 2 36 8 M30 4 L36 8 L31 12" stroke="#555" fill="none" stroke-width="1.5"/></svg>
  <svg class="abs flow-arrow" style="left:592px" width="40" height="14" viewBox="0 0 40 14"><path d="M2 10 Q20 2 36 8 M30 4 L36 8 L31 12" stroke="#555" fill="none" stroke-width="1.5"/></svg>
  <svg class="abs flow-arrow" style="left:860px" width="40" height="14" viewBox="0 0 40 14"><path d="M2 10 Q20 2 36 8 M30 4 L36 8 L31 12" stroke="#555" fill="none" stroke-width="1.5"/></svg>

  <a class="abs explore-btn">Explore More</a>
</section>

<section>
  <div class="abs work-panel"></div>
  <div class="abs label work-label">Work</div>
  <h2 class="abs heading work-heading">Latest projects</h2>
  <a class="abs view-link work-view">View All Projects &nbsp;→</a>

  <div class="abs project project-a" role="img" aria-label="Rendering of a bright villa living room with a lounge chair and fireplace"></div>
  <div class="abs project-title" style="left:130px;top:1976px">Redesign interior for villa</div>
  <div class="abs project-link" style="left:130px;top:2018px">See Project &nbsp;→</div>

  <div class="abs project project-b" role="img" aria-label="Rendering of a co-working lounge with sofas and wall shelving"></div>
  <div class="abs project-title" style="left:678px;top:1884px">Orrin co-working building</div>
  <div class="abs project-text" style="left:678px;top:1914px">Lorem Ipsum has been the industry's standard dummy text ever since the 1500s, when an unknown printer took a galley of type and scrambled it to make a type specimen book.</div>
  <div class="abs project-link" style="left:678px;top:2018px">See Project &nbsp;→</div>

  <div class="abs work-dots"><span></span><span class="on"></span><span></span><span></span><span></span></div>
</section>

<section>
  <div class="abs label test-label">Testimonials</div>
  <h2 class="abs heading test-heading">From our great clients</h2>
  <a class="abs view-link test-view">View All &nbsp;→</a>

  <div class="abs nav-circle" style="left:156px;top:2484px"><svg width="8" height="10" viewBox="0 0 8 10"><path d="M6 1 L2 5 L6 9" stroke="#ccc" fill="none" stroke-width="1.5"/></svg></div>
  <div class="abs nav-circle" style="left:1044px;top:2484px"><svg width="8" height="10" viewBox="0 0 8 10"><path d="M2 1 L6 5 L2 9" stroke="#ccc" fill="none" stroke-width="1.5"/></svg></div>

  <div class="abs quote" style="left:234px">
    <div class="avatar" role="img" aria-label="Client portrait"></div>
    <div class="quote-name">Dorian Hale, <small>CEO@Northwind Inc</small></div>
    <p class="quote-text">Lorem Ipsum has been the industry's standard dummy text ever since the 1500s, when an unknown printer took a galley of type and scrambled it to make a type specimen book ...</p>
  </div>
  <div class="abs quote" style="left:626px">
    <div class="avatar" role="img" aria-label="Client portrait"></div>
    <div class="quote-name">Lucia Verant, <small>Management@Brightloom</small></div>
    <p class="quote-text">Lorem Ipsum has been the industry's standard dummy text ever since the 1500s, when an unknown printer took a galley of type and scrambled it to make a type specimen book ...</p>
  </div>
</section>

<footer>
  <div class="abs footer-rule"></div>
  <div class="abs copyright">Copyright © 2017</div>
  <div class="abs foot-brand-row">
    <div class="foot-brand">MARA VELBOURNE</div>
    <div class="foot-sub">Interior Design LLC</div>
  </div>
  <div class="abs foot-rights">All right reserved</div>
  <ul class="abs foot-list" style="left:470px"><li>Our Story</li><li>Work</li><li>Design Process</li><li>Testimonials</li><li>Client Login</li><li>Contact</li></ul>
  <ul class="abs foot-list" style="left:680px"><li>Term &amp; Condition</li><li>Policy</li><li>Help</li></ul>
  <div class="abs contact-phone"><svg width="14" height="14" viewBox="0 0 14 14"><path d="M3 1 L5 1 L6 4 L4.5 5 Q6 8.5 9 9.5 L10 8 L13 9 L13 11 Q12 13 10 13 Q2 11 1 3 Q1 1 3 1 Z" fill="#111"/></svg>Call Us: (404) 555-0172</div>
  <div class="abs contact-mail"><svg width="14" height="12" viewBox="0 0 14 12"><rect x="1" y="1" width="12" height="10" fill="none" stroke="#111" stroke-width="1.4"/><path d="M1 1 L7 7 L13 1" fill="none" stroke="#111" stroke-width="1.4"/></svg>hello@maravelbourne.com</div>
  <div class="abs socials"><span></span><span class="on"></span><span></span></div>
</footer>

</body>
</html>
```